Business Card Design Project

we are a new company , see www.chatharborlane.com
we also have a concurrent flyer deign competition so you may also wish to enter that.
We provide live customer support services for websites.
We cater for mainly european market.
info for card:
Martin Colbrook
Director
p: +353 (0)90 612 8051
f: +353 (0)90 612 8062
m: +353 (0)86 507 4926
e: martin@chatharborlane.com
w: www.chatharborlane.com
The card does not have to use the exact colour on the website but should ahve something of the general feel of it. It should have modern corporate feel without brash coulours. we will upload the logo and card should be standard european size 85x55mm
Target Market(s)
Online business owners
Industry/Entity Type
Business
Look and feel
Each slider illustrates characteristics of the customer's brand and the style your logo design should communicate.

```html
<!DOCTYPE html>
<html lang="en">
<head>
<meta charset="utf-8">
<title>Chat Harbor Lane – Business Card</title>
<link href="https://fonts.googleapis.com/css2?family=Michroma&family=Dosis:wght@500&display=swap" rel="stylesheet">
<style>
  :root {
    --backdrop: #3a3a3a;
    --card-glow: #0f3b42;
    --card-mid: #08191d;
    --card-edge: #030708;
    --brand-blue: #3d9fd3;
    --text-light: #f2f5f6;
    --text-muted: #c9d2d4;
  }
  * { margin: 0; padding: 0; box-sizing: border-box; }
  html, body { width: 1200px; height: 900px; overflow: hidden; }
  body {
    background: var(--backdrop);
    position: relative;
    font-family: "Michroma", "Arial", sans-serif;
    color: var(--text-light);
  }
  .card {
    position: absolute;
    left: 212px;
    width: 705px;
    height: 405px;
    border-radius: 30px;
    background: radial-gradient(ellipse 70% 80% at 50% 35%, var(--card-glow) 0%, var(--card-mid) 55%, var(--card-edge) 100%);
    box-shadow: 0 4px 14px rgba(0,0,0,0.45);
    overflow: hidden;
  }
  .card--front { top: 30px; }
  .card--back { top: 470px; }

  .brand {
    position: absolute;
    left: 0; right: 0;
    display: flex;
    justify-content: center;
    align-items: center;
    gap: 14px;
    color: var(--brand-blue);
    letter-spacing: 2px;
    white-space: nowrap;
  }
  .brand__mark {
    background: var(--brand-blue);
    border-radius: 4px;
  }
  .card--front .brand { top: 150px; font-size: 38px; }
  .card--front .brand__mark { width: 30px; height: 30px; }
  .card--back .brand { top: 58px; font-size: 26px; }
  .card--back .brand__mark { width: 21px; height: 21px; }

  .tagline {
    position: absolute;
    top: 278px; left: 0; right: 0;
    text-align: center;
    font-size: 15px;
    letter-spacing: 2.5px;
    text-transform: uppercase;
  }

  .person {
    position: absolute;
    left: 40px; width: 300px;
    top: 262px;
    text-align: center;
  }
  .person__name { font-size: 17px; letter-spacing: 2.5px; text-transform: uppercase; }
  .person__role { font-size: 9px; letter-spacing: 2px; text-transform: uppercase; color: var(--text-muted); margin-top: 8px; }

  .divider {
    position: absolute;
    left: 327px; top: 217px;
    width: 4px; height: 147px;
    background: var(--text-light);
  }
  .contacts {
    position: absolute;
    left: 357px; top: 214px;
    list-style: none;
    font-family: "Dosis", "Arial", sans-serif;
    font-weight: 500;
    font-size: 17px;
    letter-spacing: 0.5px;
  }
  .contacts li {
    display: flex; align-items: center; gap: 10px;
    height: 29px;
  }
  .contacts li:last-child { margin-top: 5px; }
  .contacts svg { width: 20px; height: 20px; flex: none; fill: var(--text-light); }
</style>
</head>
<body>

<section class="card card--front">
  <div class="brand"><span class="brand__mark"></span>Chat Harbor Lane</div>
  <p class="tagline">Live Customer Support Online</p>
</section>

<section class="card card--back">
  <div class="brand"><span class="brand__mark"></span>Chat Harbor Lane</div>

  <div class="person">
    <p class="person__name">Martin Colbrook</p>
    <p class="person__role">Director</p>
  </div>

  <div class="divider"></div>

  <ul class="contacts">
    <li>
      <svg viewBox="0 0 20 20" aria-label="phone"><path d="M2 7c0-3 3-4 8-4s8 1 8 4v1h-4V6H6v2H2z"/><rect x="4" y="9" width="12" height="8" rx="1.5"/></svg>
      +353 (0)90 612 8051
    </li>
    <li>
      <svg viewBox="0 0 20 20" aria-label="fax"><rect x="5" y="2" width="10" height="6"/><rect x="2" y="8" width="16" height="9" rx="1.5"/><rect x="6" y="11" width="8" height="2" fill="#08191d"/></svg>
      +353 (0)90 612 8062
    </li>
    <li>
      <svg viewBox="0 0 20 20" aria-label="mobile"><rect x="9" y="1" width="1.5" height="4"/><rect x="6" y="4" width="8" height="15" rx="1.5"/><rect x="7.5" y="6" width="5" height="5" fill="#08191d"/></svg>
      +353 (0)86 507 4926
    </li>
    <li>
      <svg viewBox="0 0 20 20" aria-label="email"><rect x="1" y="4" width="18" height="12" rx="1.5"/><path d="M2 5l8 6 8-6" stroke="#08191d" stroke-width="1.5" fill="none"/></svg>
      martin@chatharborlane.com
    </li>
    <li>
      <svg viewBox="0 0 20 20" aria-label="website"><circle cx="10" cy="10" r="9"/><path d="M4.5 7l2 7 2-5.5 1.5 5.5 2-5.5 2 5.5 1.5-7" stroke="#08191d" stroke-width="1.6" fill="none" stroke-linejoin="round"/></svg>
      www.chatharborlane.com
    </li>
  </ul>
</section>

</body>
</html>
```